DJ Kovan Threl

I'm looking for a professional but still artsy/progressive design. I come from a hip hop/club DJ background playing a lot of underground music but have switched to doing more corporate parties and weddings recently. I am all about keeping the dancefloor moving and emotionally connecting with the crowd. I'd like a trendy/updated color palette. Something that's clean enough that looks professional but also trendy enough to convey that by the end of the night we'll be sweatily dancing to the latest hits. Some designers/artists I like: Rolo Partague, Wendel Ashby, Tobiah Crane, Vexmor 3100, Lyle Brandish.

```html
<!DOCTYPE html>
<html lang="en">
<head>
<meta charset="utf-8">
<title>DJ Kovan Threl — Business Card</title>
<link rel="stylesheet" href="https://fonts.googleapis.com/css2?family=Fira+Sans+Condensed:wght@400;700&display=swap">
<style>
  :root {
    --backdrop: #d0d2cf;
    --card-white: #f3f2f4;
    --ink: #1e1c1d;
    --paper-text: #ffffff;
    --paint-blue: #5b80c8;
    --paint-indigo: #3a3f9a;
    --paint-green: #4a8a6c;
    --paint-pink: #c2588a;
    --paint-white: #e8e9f0;
  }
  html, body {
    margin: 0;
    padding: 0;
    width: 1200px;
    height: 876px;
    overflow: hidden;
    background: var(--backdrop);
  }
  .canvas {
    position: relative;
    width: 1200px;
    height: 876px;
    font-family: "Fira Sans Condensed", "Arial Narrow", sans-serif;
  }
  .card {
    position: absolute;
    left: 255px;
    width: 672px;
    height: 419px;
  }
  .card--front { top: 8px; }
  .card--back {
    top: 443px;
    background: var(--card-white);
  }
  .front-artwork {
    position: absolute;
    inset: 0;
    background:
      radial-gradient(circle at 15% 30%, var(--paint-green) 0, transparent 28%),
      radial-gradient(circle at 85% 45%, var(--paint-pink) 0, transparent 30%),
      radial-gradient(circle at 55% 20%, var(--paint-white) 0, transparent 25%),
      linear-gradient(135deg, var(--paint-blue), var(--paint-indigo) 60%, var(--paint-blue));
  }
  .front-name {
    position: absolute;
    left: 0;
    right: 0;
    top: 172px;
    margin: 0;
    text-align: center;
    font-weight: 700;
    font-size: 60px;
    line-height: 1;
    color: var(--paper-text);
  }
  .back-name {
    position: absolute;
    left: 56px;
    top: 168px;
    margin: 0;
    font-weight: 700;
    font-size: 32px;
    line-height: 1;
    color: var(--ink);
  }
  .contact-list {
    position: absolute;
    margin: 0;
    padding: 0;
    list-style: none;
    color: var(--ink);
    font-weight: 400;
    font-size: 17px;
  }
  .contact-list li {
    position: absolute;
    display: flex;
    align-items: center;
    gap: 8px;
    white-space: nowrap;
  }
  .contact-list svg { width: 20px; height: 20px; fill: var(--ink); flex: none; }
  .contact-phone { left: 429px; top: 160px; }
  .contact-email { left: 403px; top: 187px; }
  .contact-web   { left: 384px; top: 217px; }
</style>
</head>
<body>
<main class="canvas">
  <section class="card card--front">
    <div class="front-artwork" role="img" aria-label="Abstract splattered graffiti painting in blue, purple, green, pink and white"></div>
    <h1 class="front-name">DJ Kovan Threl</h1>
  </section>

  <section class="card card--back">
    <p class="back-name">DJ Kovan Threl</p>
    <ul class="contact-list">
      <li class="contact-phone">
        <svg viewBox="0 0 24 24" aria-hidden="true"><path d="M6.6 10.8a15.1 15.1 0 0 0 6.6 6.6l2.2-2.2a1 1 0 0 1 1-.25 11.4 11.4 0 0 0 3.6.57 1 1 0 0 1 1 1V20a1 1 0 0 1-1 1A17 17 0 0 1 3 4a1 1 0 0 1 1-1h3.5a1 1 0 0 1 1 1c0 1.25.2 2.45.57 3.57a1 1 0 0 1-.25 1z"/></svg>
        <span>+00 1234 567 889</span>
      </li>
      <li class="contact-email">
        <svg viewBox="0 0 24 24" aria-hidden="true"><path d="M22 2 2 10.5l7 2.6L20 5l-8.6 9.4V22l3.9-5.2 4.7 3.2z"/></svg>
        <span>yourname@mailpost.com</span>
      </li>
      <li class="contact-web">
        <svg viewBox="0 0 24 24" aria-hidden="true"><path d="M12 2a10 10 0 1 0 0 20 10 10 0 0 0 0-20zm6.9 6h-2.9a15.6 15.6 0 0 0-1.4-3.6A8 8 0 0 1 18.9 8zM12 4c.8 1.2 1.5 2.5 1.9 4h-3.8c.4-1.5 1.1-2.8 1.9-4zM4.3 14a8 8 0 0 1 0-4h3.4a16 16 0 0 0 0 4zm.8 2h2.9c.3 1.3.8 2.5 1.4 3.6A8 8 0 0 1 5.1 16zM8 8H5.1a8 8 0 0 1 4.3-3.6C8.8 5.5 8.3 6.7 8 8zm4 12c-.8-1.2-1.5-2.5-1.9-4h3.8c-.4 1.5-1.1 2.8-1.9 4zm2.3-6H9.7a14.6 14.6 0 0 1 0-4h4.6a14.6 14.6 0 0 1 0 4zm.3 5.6c.6-1.1 1.1-2.3 1.4-3.6h2.9a8 8 0 0 1-4.3 3.6zm1.7-5.6a16 16 0 0 0 0-4h3.4a8 8 0 0 1 0 4z"/></svg>
        <span>www.yoursite.com</span>
      </li>
    </ul>
  </section>
</main>
</body>
</html>
```